Management consultant needs to update look of website

Currently I have a great word press website but it needs an updated look. I have new text for the site in the attached word document. I also have a list of websites whose design, look, and organization i like as a guide for the designer. The final design should be simple, strong, clear, and project the idea that my brand is a powerful authority in this space. Current site = www.brookfernadvisory.com

Target Market(s)

company owners / executives

Industry/Entity Type

Management Consulting

Number of Pages Required

3 page

Font styles to use
Serif

Colors

Designer to choose colors to be used in the design.

Requirements
Must have
• a simple and clear design and message. professional look. easy navigation. responsive to mobile devices. an easily implemented wordpress theme OR squarespace. use of my logo colors. though I am open to changing to a deep navy or charcoal logo image. source file uploaded.
Nice to have
• i like the cover photo and logo watermark on my current homepage. i like the google map with my logo on the current contact page. i like the animation as well. a great blend of the current site and something that is more seamless.

```html
<!DOCTYPE html>
<html lang="en">
<head>
<meta charset="utf-8">
<title>Brookfern Advisory — Leadership, Workshops, Coaching</title>
<link rel="stylesheet" href="https://fonts.googleapis.com/css2?family=Libre+Baskerville:wght@400;700&family=Lato:wght@400;700&display=swap">
<style>
:root{
  --gold:#a8883a;
  --gold-dark:#8d7030;
  --red:#c4261d;
  --ink:#2b2b2b;
  --text:#4a4a4a;
  --muted:#8a8a8a;
  --line:#d8d8d8;
  --mist:#f1f1f1;
  --night:#1d1d1d;
  --white:#ffffff;
  --slate:#8c8c8c;
}
*{margin:0;padding:0;box-sizing:border-box}
html,body{width:1200px;height:4063px;overflow:hidden}
body{position:relative;background:var(--white);font-family:"Lato",sans-serif;color:var(--text)}
section,header,footer{position:absolute;left:0;width:1200px}
.abs{position:absolute}

/* header */
.site-header{top:0;height:179px;z-index:3}
.navbar{left:0;top:130px;width:1200px;height:49px;background:var(--gold)}
.nav{position:absolute;left:0;top:0;width:1200px;height:49px;list-style:none}
.nav li{position:absolute;top:0;height:49px;display:flex;align-items:center;font-family:"Libre Baskerville",serif;font-size:15px;color:var(--white);text-transform:uppercase;white-space:nowrap}
.nav li.active{background:var(--slate);padding:0 26px}
.brand{left:70px;top:10px;width:252px;text-align:center;background:var(--white);padding-bottom:6px;z-index:2}
.brand-mark{width:92px;height:92px;border-radius:50%;background:var(--gold);margin:0 auto 6px}
.brand-name{font-family:"Libre Baskerville",serif;font-size:23px;color:var(--gold);letter-spacing:1px;text-transform:uppercase;line-height:1.2}
.brand-tag{font-size:10.5px;color:var(--gold);letter-spacing:1.3px;text-transform:uppercase;margin-top:3px;white-space:nowrap}
.contact-top{top:44px;font-size:13px;color:var(--ink);display:flex;align-items:center;gap:12px;white-space:nowrap}
.contact-top .ico{width:38px;height:38px;border-radius:50%;border:2px solid var(--gold);display:flex;align-items:center;justify-content:center;flex:none}
.contact-top small{display:block;font-size:12px;letter-spacing:1px;text-transform:uppercase}
.contact-top b{font-size:16px}

/* hero */
.hero{top:179px;height:560px}
.hero-photo{position:absolute;inset:0;background:linear-gradient(120deg,#5b5048 0%,#8a7c6e 35%,#b9b1a6 60%,#6f6256 100%)}
.hero-badge{left:475px;top:92px;width:270px;height:270px;border-radius:50%;background:rgba(70,60,50,.75);display:flex;align-items:center;justify-content:center;text-align:center;font-family:"Libre Baskerville",serif;font-weight:700;font-size:30px;line-height:1.45;color:var(--white);text-transform:uppercase}
.hero-curve{position:absolute;left:0;bottom:0}

/* headings */
.sec-title{width:1200px;text-align:center;font-family:"Libre Baskerville",serif;font-size:36px;color:var(--ink);text-transform:uppercase;letter-spacing:1px}
.sec-title em{font-style:normal;color:var(--red)}
.sec-title.gold em{color:var(--gold)}
.title-rule{left:450px;width:300px;height:20px}

/* services */
.services{top:737px;height:630px}
.service{top:217px;width:325px;height:308px;text-align:center;padding-top:8px}
.service.featured{border:2px solid #e3a7a3;border-radius:8px}
.service .icon{width:110px;height:110px;border-radius:50%;margin:0 auto;border:3px solid var(--gold);background:#efe6d2}
.service.featured .icon{background:var(--gold);border-color:var(--gold)}
.service h3{font-family:"Libre Baskerville",serif;font-size:15px;text-transform:uppercase;color:var(--ink);margin-top:22px;line-height:1.3}
.service.featured h3{color:var(--gold)}
.service p{font-size:14px;line-height:1.6;margin:14px 26px 0}
.readmore{display:inline-block;font-size:12px;color:var(--muted);text-transform:uppercase;text-decoration:underline;margin-top:16px}

/* about */
.about{top:1368px;height:534px;background:var(--gold)}
.about-mark{left:-28px;top:26px;width:490px;height:490px;border-radius:50%;background:var(--white);display:flex;align-items:center;justify-content:center}
.about-mark span{font-family:"Libre Baskerville",serif;font-size:30px;color:var(--gold);text-transform:uppercase;text-align:center;line-height:1.4}
.about h2{left:496px;top:98px;font-family:"Libre Baskerville",serif;font-size:33px;color:var(--white);text-transform:uppercase;font-weight:400;white-space:nowrap}
.about h2 b{font-weight:700}
.about-rule{left:496px;top:155px;width:610px;height:1px;background:rgba(255,255,255,.6)}
.about-copy{left:496px;top:190px;width:620px;font-size:14.5px;line-height:1.65;color:var(--white)}
.about-copy p+p{margin-top:12px}
.btn-pill{left:492px;top:469px;width:178px;height:45px;border-radius:23px;background:#7a7a7a;border:2px solid #d2d2d2;color:var(--white);font-size:14px;display:flex;align-items:center;justify-content:center;text-transform:uppercase;letter-spacing:1px}

/* testimonials */
.testimonials{top:1902px;height:495px}
.quote{top:218px;width:326px;text-align:center}
.quote h4{font-family:"Libre Baskerville",serif;font-size:16px;font-weight:400;text-transform:uppercase;color:var(--ink)}
.quote.featured h4{color:var(--gold)}
.stars{color:var(--gold);font-size:16px;letter-spacing:3px;margin-top:4px}
.quote .box{margin-top:14px;height:116px;border:1px solid var(--line);box-shadow:0 3px 6px rgba(0,0,0,.12);text-align:left;padding:18px 24px;font-size:14px;line-height:1.55;color:var(--text)}
.quote.featured .box{border-bottom:3px solid var(--gold)}
.q{font-family:"Libre Baskerville",serif;font-size:24px;color:var(--gold);line-height:0}
.carousel-arrow{width:20px;height:40px}

/* blog */
.blog{top:2397px;height:664px;background:var(--mist)}
.blog-intro{top:212px;width:1200px;text-align:center;font-size:13.5px;color:var(--ink)}
.post{top:320px;width:500px;height:262px;background:var(--white);border:1px solid var(--line);border-radius:14px}
.post-thumb{top:-36px;left:22px;width:150px;height:150px;border-radius:50%;border:5px solid var(--white);box-shadow:0 2px 6px rgba(0,0,0,.2)}
.post h3{position:absolute;left:192px;top:30px;width:290px;font-family:"Libre Baskerville",serif;font-size:16px;line-height:1.3;color:var(--gold);text-transform:uppercase}
.post .meta{position:absolute;left:192px;top:86px;font-size:13px;color:var(--ink)}
.post .excerpt{position:absolute;left:22px;top:120px;width:456px;font-size:14px;line-height:1.6;color:var(--ink)}
.post .readmore{position:absolute;left:22px;top:224px;margin:0}

/* clients */
.clients{top:3088px;height:596px}
.client{width:192px;height:86px;border:1px solid var(--line);border-radius:6px;box-shadow:0 2px 4px rgba(0,0,0,.1);display:flex;align-items:center;justify-content:center;gap:8px;font-weight:700;font-size:16px;color:#555}
.client i{width:14px;height:14px;border-radius:50%;background:var(--gold);display:block}

/* footer */
.site-footer{top:3684px;height:325px;background:var(--night);color:#d8d8d8}
.f-col h5{font-family:"Libre Baskerville",serif;font-size:15px;font-weight:400;text-transform:uppercase;color:var(--white)}
.f-col h5 b{font-weight:700}
.f-rule{height:1px;background:#555;margin-top:10px}
.f-links{list-style:none;margin-top:18px}
.f-links li{font-size:14px;margin-bottom:14px}
.f-links li::before{content:"›";margin-right:8px}
.f-addr{font-size:13.5px;line-height:1.45}
.f-line{display:flex;align-items:center;gap:10px;font-size:14px;margin-top:24px}
.field{width:256px;height:30px;border:1px solid #777;border-radius:4px;margin-top:8px;padding:6px 10px;font-size:13px;color:#ddd}
.field.tall{height:56px}
.submit{display:inline-block;margin-top:10px;background:#7a7a7a;color:var(--white);font-size:12px;padding:7px 20px;border-radius:14px;text-transform:uppercase}
.footer-mark{left:880px;top:30px;width:270px;height:270px;border-radius:50%;background:var(--gold);display:flex;align-items:center;justify-content:center;font-family:"Libre Baskerville",serif;font-size:20px;color:var(--night);text-transform:uppercase;text-align:center;line-height:1.4}
.copybar{left:0;top:4009px;width:1200px;height:54px;background:var(--gold)}
.copybar p{position:absolute;left:81px;top:18px;font-size:13px;color:var(--white);white-space:nowrap}
.social{top:12px;width:30px;height:30px;border-radius:50%;background:#2c4a7a}
</style>
</head>
<body>

<header class="site-header">
  <nav class="navbar abs">
    <ul class="nav">
      <li class="active" style="left:320px">Home</li>
      <li style="left:452px">About Us</li>
      <li style="left:610px">Our Services</li>
      <li style="left:807px">Our Clients</li>
      <li style="left:997px">Contact Us</li>
    </ul>
  </nav>
  <div class="brand abs">
    <div class="brand-mark"></div>
    <div class="brand-name">Brookfern Advisory</div>
    <div class="brand-tag">Strategy · Workshops · Coaching</div>
  </div>
  <div class="contact-top abs" style="left:672px">
    <span class="ico"><svg width="18" height="18" viewBox="0 0 24 24"><path d="M6.6 10.8a15 15 0 006.6 6.6l2.2-2.2c.3-.3.7-.4 1-.2 1.1.4 2.3.6 3.6.6.6 0 1 .4 1 1V20c0 .6-.4 1-1 1A17 17 0 013 4c0-.6.4-1 1-1h3.5c.6 0 1 .4 1 1 0 1.3.2 2.5.6 3.6.1.3 0 .7-.2 1z" fill="#2b2b2b"/></svg></span>
    <span><small>Call us today</small><b>555.014.2290</b></span>
  </div>
  <div class="contact-top abs" style="left:888px">
    <span class="ico"><svg width="18" height="14" viewBox="0 0 24 18"><rect x="1" y="1" width="22" height="16" rx="2" fill="none" stroke="#2b2b2b" stroke-width="2"/><path d="M1 2l11 8 11-8" fill="none" stroke="#2b2b2b" stroke-width="2"/></svg></span>
    <span><small>Email us</small><b>info@brookfernadvisory.com</b></span>
  </div>
</header>

<section class="hero">
  <div class="hero-photo" role="img" aria-label="Photo of a leadership workshop: a facilitator presenting to a team seated around a table"></div>
  <div class="hero-badge abs">Leadership<br>Team<br>Development</div>
  <svg class="hero-curve" width="1200" height="150" viewBox="0 0 1200 150">
    <path d="M0 0 C250 110 950 110 1200 0 L1200 150 L0 150 Z" fill="#ffffff"/>
    <path d="M0 20 C260 150 940 150 1200 20 L1200 40 C940 140 260 140 0 40 Z" fill="#a8883a"/>
  </svg>
</section>

<section class="services">
  <h2 class="sec-title abs" style="top:104px">Our <em>Services</em></h2>
  <svg class="title-rule abs" style="top:154px" viewBox="0 0 300 20"><line x1="0" y1="10" x2="130" y2="10" stroke="#d8d8d8"/><line x1="170" y1="10" x2="300" y2="10" stroke="#d8d8d8"/><circle cx="150" cy="10" r="9" fill="none" stroke="#a8883a" stroke-width="2"/><circle cx="150" cy="10" r="4" fill="#a8883a"/></svg>

  <div class="service abs" style="left:81px">
    <div class="icon" role="img" aria-label="Icon of a person at the centre of a team"></div>
    <h3>Talent<br>Strategy</h3>
    <p>Business growth, even in the beginning, comes down to hiring the right talent and putting them in the right position to succeed..</p>
    <span class="readmore">Read more »</span>
  </div>
  <div class="service featured abs" style="left:433px">
    <div class="icon" role="img" aria-label="Icon of people meeting around a table"></div>
    <h3>Management<br>Workshops</h3>
    <p>Bringing an expert in-house to get your leaders on the same page in terms of how to manage, how to lead, and how to show..</p>
    <span class="readmore">Read more »</span>
  </div>
  <div class="service abs" style="left:791px">
    <div class="icon" role="img" aria-label="Icon of two people in a coaching conversation"></div>
    <h3>Executive<br>Coaching</h3>
    <p>I can be incredibly challenging to push yourself, or you company, to the next level without viewing things from..</p>
    <span class="readmore">Read more »</span>
  </div>
</section>

<section class="about">
  <div class="about-mark abs"><span>Brookfern<br>Advisory</span></div>
  <h2 class="abs">About <b>Brookfern Advisory</b></h2>
  <div class="about-rule abs"></div>
  <div class="about-copy abs">
    <p>Dr. Elena Marsh is a business consultant, group trainer, and executive coach specializing in workplace culture, leadership development, and managerial tactics. The founder and director of Brookfern Advisory, she serves as an executive education instructor at Hollins State University's School of Business.</p>
    <p>Dr. Marsh has earned multiple teaching awards throughout her career thanks to her ability to approach learners from every generation with skill and grace, and she has spent more than 20 years studying the science behind group dynamics, identity, emotion, and the social construction of one's self.</p>
  </div>
  <div class="btn-pill abs">Read more »</div>
</section>

<section class="testimonials">
  <h2 class="sec-title gold abs" style="top:96px">Client <em>Testimonials</em></h2>
  <svg class="title-rule abs" style="top:146px" viewBox="0 0 300 20"><line x1="0" y1="10" x2="130" y2="10" stroke="#d8d8d8"/><line x1="170" y1="10" x2="300" y2="10" stroke="#d8d8d8"/><circle cx="150" cy="10" r="9" fill="none" stroke="#a8883a" stroke-width="2"/><circle cx="150" cy="10" r="4" fill="#a8883a"/></svg>
  <svg class="carousel-arrow abs" style="left:40px;top:318px" viewBox="0 0 20 40"><path d="M16 4L4 20l12 16" fill="none" stroke="#cfcfcf" stroke-width="3"/></svg>
  <svg class="carousel-arrow abs" style="left:1140px;top:318px" viewBox="0 0 20 40"><path d="M4 4l12 16L4 36" fill="none" stroke="#cfcfcf" stroke-width="3"/></svg>

  <div class="quote featured abs" style="left:81px">
    <h4>Mark R</h4><div class="stars">★★★★★</div>
    <div class="box"><span class="q">“</span> Elena Marsh is an outstanding leadership facilitator and professional. I had the opportunity to work with her in facilitating a..[+] <span class="q">”</span></div>
  </div>
  <div class="quote abs" style="left:433px">
    <h4>Paul Doran</h4><div class="stars">★★★★★</div>
    <div class="box"><span class="q">“</span> After working in the consulting business for 12 years, I met Elena. I was immediately impressed by her ability to ask the..[+] <span class="q">”</span></div>
  </div>
  <div class="quote abs" style="left:791px">
    <h4>Ruth Calder</h4><div class="stars">★★★★★</div>
    <div class="box"><span class="q">“</span> She listened closely, asked sharp questions and left our leaders with a clear plan they still use..[+] <span class="q">”</span></div>
  </div>
</section>

<section class="blog">
  <h2 class="sec-title gold abs" style="top:100px"><span style="color:var(--ink)">Recent</span> <em>Blog Posts</em></h2>
  <svg class="title-rule abs" style="top:150px" viewBox="0 0 300 20"><line x1="0" y1="10" x2="130" y2="10" stroke="#cfcfcf"/><line x1="170" y1="10" x2="300" y2="10" stroke="#cfcfcf"/><circle cx="150" cy="10" r="9" fill="none" stroke="#a8883a" stroke-width="2"/><circle cx="150" cy="10" r="4" fill="#a8883a"/></svg>
  <p class="blog-intro abs">Brookfern Advisory Insights Blog will help you gain perspective on yourself, your organization, and how to reach your potential at work:</p>
  <svg class="carousel-arrow abs" style="left:40px;top:432px" viewBox="0 0 20 40"><path d="M16 4L4 20l12 16" fill="none" stroke="#cfcfcf" stroke-width="3"/></svg>
  <svg class="carousel-arrow abs" style="left:1140px;top:432px" viewBox="0 0 20 40"><path d="M4 4l12 16L4 36" fill="none" stroke="#cfcfcf" stroke-width="3"/></svg>

  <article class="post abs" style="left:81px">
    <div class="post-thumb abs" style="background:linear-gradient(135deg,#8a7a6a,#cbbfb0)" role="img" aria-label="Photo of a young professional starting a new job"></div>
    <h3>The Show-Up-On-Time Rule</h3>
    <div class="meta">September 29, 2017 &nbsp;&nbsp; ▢ (0) Comments</div>
    <p class="excerpt">recent college grad asked me for advice on how to succeed with a new job. And this was it. To "show-up-on-time." Likewise, a company owner recently asked me for advice on how to build morale in their office. And this was it. To "show-up-on-time." It doesn't matter if you are the newest..</p>
    <span class="readmore">Read more »</span>
  </article>
  <article class="post abs" style="left:624px">
    <div class="post-thumb abs" style="background:linear-gradient(135deg,#6f5a44,#c9a878)" role="img" aria-label="Photo of an interview in progress sign"></div>
    <h3>How to Ask Great Interview Questions</h3>
    <div class="meta">September 10, 2017 &nbsp;&nbsp; ▢ (0) Comments</div>
    <p class="excerpt">If you are a manger, you are well aware that hiring the wrong person can destroy a department. Hiring the right person – every time – is the ultimate goal. So how can you ask interview questions that successfully weed out potential bad seeds? Here are 4 strategies to adopt.</p>
    <span class="readmore">Read more »</span>
  </article>
</section>

<section class="clients">
  <h2 class="sec-title abs" style="top:80px">Clients <em>&amp; Partners</em></h2>
  <svg class="title-rule abs" style="top:130px" viewBox="0 0 300 20"><line x1="0" y1="10" x2="130" y2="10" stroke="#d8d8d8"/><line x1="170" y1="10" x2="300" y2="10" stroke="#d8d8d8"/><circle cx="150" cy="10" r="9" fill="none" stroke="#a8883a" stroke-width="2"/><circle cx="150" cy="10" r="4" fill="#a8883a"/></svg>

  <div class="client abs" style="left:81px;top:198px"><i></i>Cedar Library</div>
  <div class="client abs" style="left:291px;top:198px"><i></i>Northgate</div>
  <div class="client abs" style="left:501px;top:198px"><i></i>Kestrel</div>
  <div class="client abs" style="left:712px;top:198px"><i></i>Ridgeway</div>
  <div class="client abs" style="left:923px;top:198px"><i></i>Amberly</div>

  <div class="client abs" style="left:81px;top:304px"><i></i>Elmfield</div>
  <div class="client abs" style="left:291px;top:304px"><i></i>Timberline</div>
  <div class="client abs" style="left:501px;top:304px"><i></i>Crestpoint</div>
  <div class="client abs" style="left:712px;top:304px"><i></i>Harbor Growth</div>
  <div class="client abs" style="left:923px;top:304px"><i></i>Foldwell</div>

  <div class="client abs" style="left:81px;top:407px"><i></i>Oakline Grill</div>
  <div class="client abs" style="left:291px;top:407px"><i></i>Pryor &amp; Partners</div>
  <div class="client abs" style="left:501px;top:407px"><i></i>Cedar Library</div>
  <div class="client abs" style="left:712px;top:407px"><i></i>Elmfield</div>
  <div class="client abs" style="left:923px;top:407px"><i></i>Ridgeway</div>
</section>

<footer class="site-footer">
  <div class="f-col abs" style="left:81px;top:48px;width:160px">
    <h5>Quick <b>Links</b></h5>
    <div class="f-rule"></div>
    <ul class="f-links">
      <li>Home</li><li>About Us</li><li>Our Services</li><li>Our Clients</li><li>Contact Us</li>
    </ul>
  </div>
  <div class="f-col abs" style="left:256px;top:48px;width:250px">
    <h5>Contact <b>Details</b></h5>
    <div class="f-rule"></div>
    <div class="f-line" style="align-items:flex-start;margin-top:18px">
      <svg width="14" height="18" viewBox="0 0 14 20"><path d="M7 0a7 7 0 00-7 7c0 5 7 13 7 13s7-8 7-13a7 7 0 00-7-7zm0 9.5A2.5 2.5 0 117 4.5a2.5 2.5 0 010 5z" fill="#d8d8d8"/></svg>
      <div class="f-addr"><b>BROOKFERN ADVISORY</b><br>Riverside Business Center<br>118 Mill Street<br>Easton, GA 30999</div>
    </div>
    <div class="f-line"><svg width="16" height="16" viewBox="0 0 24 24"><path d="M6.6 10.8a15 15 0 006.6 6.6l2.2-2.2c.3-.3.7-.4 1-.2 1.1.4 2.3.6 3.6.6.6 0 1 .4 1 1V20c0 .6-.4 1-1 1A17 17 0 013 4c0-.6.4-1 1-1h3.5c.6 0 1 .4 1 1 0 1.3.2 2.5.6 3.6.1.3 0 .7-.2 1z" fill="#d8d8d8"/></svg>555.014.2290</div>
    <div class="f-line"><svg width="16" height="12" viewBox="0 0 24 18"><rect x="1" y="1" width="22" height="16" rx="2" fill="none" stroke="#d8d8d8" stroke-width="2"/><path d="M1 2l11 8 11-8" fill="none" stroke="#d8d8d8" stroke-width="2"/></svg>info@brookfernadvisory.com</div>
  </div>
  <div class="f-col abs" style="left:572px;top:48px;width:280px">
    <h5>Quick <b>Inquiry</b></h5>
    <div class="f-rule"></div>
    <div class="field" style="margin-top:14px">Your Name</div>
    <div class="field">Phone</div>
    <div class="field">Email</div>
    <div class="field tall">Message</div>
    <span class="submit">Submit »</span>
  </div>
  <div class="footer-mark abs">Brookfern<br>Advisory</div>
</footer>

<div class="copybar abs">
  <p>Copyright © 2019 Brookfern Advisory, LLC. All Rights Reserved.</p>
  <span class="social abs" style="left:972px" aria-label="Social profile"></span>
  <span class="social abs" style="left:1010px" aria-label="Social profile"></span>
  <span class="social abs" style="left:1048px" aria-label="Social profile"></span>
</div>

</body>
</html>
```